Brightpath Dentistry - Flyer - Modern & Eye catching campaign flyer

Need front & back side full page flyer designs for both 1) Grand opening 2) On-going campaign.

Attached the new dental office logo.
Attached our other dental clinic flyer designs for content.

Target Market(s)

Cosmetic dentistry

Industry/Entity Type

Health Care

Requirements
Must have
• decent, modern and eye catching marketing flyers.
Nice to have
• - Nice space
• - Highlight phone number
• - Highlight special features like convenient hours, call or text, for all ages, digital facility, etc
Should not have
• - Don't want to fill the flyer with too much wordings
• - Too many colors

```html
<!DOCTYPE html>
<html lang="en">
<head>
<meta charset="utf-8">
<title>Brightpath Dentistry – Grand Opening Flyer</title>
<link rel="stylesheet" href="https://fonts.googleapis.com/css2?family=Montserrat:wght@500;600;700;800;900&display=swap">
<style>
  :root {
    --frame-blue: #3f74b8;
    --panel-blue: #2b5c9c;
    --box-blue: #234d86;
    --navy: #16325c;
    --tooth-blue: #2f66ad;
    --orange: #f39a1e;
    --white: #ffffff;
    --ice: #dfeaf7;
  }
  * { box-sizing: border-box; margin: 0; padding: 0; }
  html, body { width: 876px; height: 1200px; overflow: hidden; background: var(--white); }
  body { font-family: "Montserrat", Arial, sans-serif; color: var(--white); }

  .flyer {
    position: relative;
    width: 876px;
    height: 1200px;
    background: var(--frame-blue);
    overflow: hidden;
  }
  .panel {
    position: absolute;
    left: 30px; right: 30px; top: 30px; bottom: 30px;
    background: var(--panel-blue);
  }
  .header {
    position: absolute;
    left: 0; right: 0; top: 0;
    height: 150px;
    background: var(--white);
  }
  .header-curve {
    position: absolute;
    left: 0; top: 148px;
    width: 876px; height: 60px;
  }
  .brand {
    position: absolute;
    top: 50px; left: 0; right: 0;
    display: flex; align-items: center; justify-content: center; gap: 16px;
  }
  .brand-dot {
    width: 40px; height: 40px; border-radius: 50%;
    background: var(--tooth-blue);
  }
  .brand-name {
    font-weight: 800;
    font-size: 40px;
    letter-spacing: 2px;
    color: var(--tooth-blue);
    text-transform: uppercase;
  }

  .insurance-badge {
    position: absolute;
    left: 705px; top: 178px;
    width: 104px; height: 104px;
    border-radius: 50%;
    background: var(--navy);
    border: 3px solid var(--white);
    display: flex; align-items: center; justify-content: center;
    text-align: center;
    font-size: 11px; font-weight: 700; line-height: 1.35;
    text-transform: uppercase;
  }

  .hero-art {
    position: absolute;
    left: 215px; top: 236px;
    width: 446px; height: 322px;
    border-radius: 150px 150px 90px 90px / 130px 130px 80px 80px;
    background: linear-gradient(180deg, var(--white) 60%, var(--ice) 100%);
  }
  .hero-title {
    position: absolute;
    left: 0; right: 0; top: 302px;
    text-align: center;
    color: var(--tooth-blue);
    font-weight: 800;
    font-size: 72px;
    line-height: 1.18;
    text-transform: uppercase;
  }

  .service-title {
    position: absolute;
    left: 0; right: 0; top: 690px;
    text-align: center;
    color: var(--orange);
    font-weight: 800;
    font-size: 40px;
    line-height: 1.15;
    text-transform: uppercase;
  }
  .features {
    position: absolute;
    left: 168px; width: 540px; top: 840px;
    padding: 20px 16px;
    background: var(--box-blue);
    border-radius: 14px;
    list-style: none;
    text-align: center;
    font-weight: 700;
    font-size: 14.5px;
    line-height: 2;
    white-space: nowrap;
  }

  .cta-label {
    position: absolute;
    left: 0; right: 0; top: 1040px;
    text-align: center;
    font-weight: 600;
    font-size: 25px;
    text-transform: uppercase;
  }
  .phone-pill {
    position: absolute;
    left: 250px; top: 1088px;
    width: 376px; height: 68px;
    border-radius: 34px;
    background: var(--orange);
    display: flex; align-items: center;
  }
  .phone-icon {
    width: 68px; height: 68px; border-radius: 50%;
    background: var(--white);
    border: 4px solid var(--orange);
    display: flex; align-items: center; justify-content: center;
    flex-shrink: 0;
  }
  .phone-number {
    flex: 1;
    text-align: center;
    font-weight: 800;
    font-size: 42px;
    padding-right: 12px;
  }

  .side-contact {
    position: absolute;
    left: 44px; top: 860px;
    transform-origin: left top;
    transform: rotate(-90deg);
    font-size: 9px; font-weight: 500;
    white-space: nowrap;
    opacity: 0.85;
    display: flex; gap: 30px;
  }
</style>
</head>
<body>
<main class="flyer">
  <section class="panel"></section>

  <header class="header">
    <div class="brand">
      <span class="brand-dot"></span>
      <span class="brand-name">Brightpath Dentistry</span>
    </div>
  </header>
  <svg class="header-curve" viewBox="0 0 876 60" aria-hidden="true">
    <path d="M0 0 H876 V10 H110 Q55 10 30 60 H0 Z" fill="#ffffff"/>
  </svg>

  <div class="insurance-badge">All<br>Insurances<br>Accepted</div>

  <div class="hero-art" role="img" aria-label="Large white tooth with a cut ribbon, scissors and confetti"></div>
  <h1 class="hero-title">Grand<br>Opening</h1>

  <h2 class="service-title">Family &amp; Cosmetic<br>Dentistry</h2>

  <ul class="features">
    <li>State-of-the-art equipment and paperless facility</li>
    <li>Filled with entertainment devices for patient comfort.</li>
    <li>Same-day appointment for DENTAL EMERGENCIES</li>
    <li>Helping community with routine free kids dental screening.</li>
  </ul>

  <p class="cta-label">Call or Text us now</p>
  <div class="phone-pill">
    <span class="phone-icon">
      <svg width="30" height="30" viewBox="0 0 24 24" aria-hidden="true">
        <path fill="#f39a1e" d="M6.6 10.8a15.1 15.1 0 0 0 6.6 6.6l2.2-2.2a1 1 0 0 1 1-.25 11.4 11.4 0 0 0 3.6.57 1 1 0 0 1 1 1V20a1 1 0 0 1-1 1A17 17 0 0 1 3 4a1 1 0 0 1 1-1h3.5a1 1 0 0 1 1 1c0 1.25.2 2.45.57 3.57a1 1 0 0 1-.25 1z"/>
      </svg>
    </span>
    <span class="phone-number">610-555-0148</span>
  </div>

  <div class="side-contact">
    <span>www.brightpathdental.com</span>
    <span>hello@brightpathdental.com</span>
  </div>
</main>
</body>
</html>
```